ROV Medisource Website design
Website design
ROV Medisource Website design -
Creative Brief
www.rovmedisource.example
Leading exporter for used medical equipments world wide
Like it to me clean and simple
left side
http://www.bluvantor.example/ http://www.torrelinkmd.example/index.html http://www.quovarent.example/en.html http://www.halbrit.example/ http://www.wellgatehub.example/ http://www.vintrosa.example/home http://www.carelodgex.example/ http://www.dorum.example/ http://www.ferntonmed.example/ http://www.zavrimedix.example/ http://www.pinehursthomes.example/ http://www.gluvatrade.example/component/page,shop.browse/category_id,8/option,com_virtuemart/Itemid,64/ (Left hand Navigation for Equipment page)

```html
<!DOCTYPE html>
<html lang="en">
<head>
<meta charset="utf-8">
<title>ROV Medisource – Website Design</title>
<link href="https://fonts.googleapis.com/css2?family=Open+Sans:wght@400;600;700&display=swap" rel="stylesheet">
<style>
  :root {
    --canvas: #ffffff;
    --ink: #3d4a55;
    --muted: #6f7c86;
    --brand: #2a6fb0;
    --brand-dark: #1b4f86;
    --nav: #3f86c4;
    --nav-dark: #2c6aa5;
    --banner-a: #e6f2fb;
    --banner-b: #bcdcf2;
    --photo-a: #8cc0e4;
    --photo-b: #2c6fa8;
    --side-head: #d9ebf8;
    --rule: #d4e2ec;
    --footer: #f2f6f9;
    --accent: #c8342c;
  }
  * { box-sizing: border-box; margin: 0; padding: 0; }
  html, body { width: 1200px; height: 583px; overflow: hidden; background: var(--canvas); }
  body { position: relative; font-family: "Open Sans", Arial, sans-serif; color: var(--ink); }

  .page { position: absolute; background: #fff; overflow: hidden; box-shadow: 0 0 0 1px #eef2f5; }
  .page--home { left: 0; top: 0; width: 396px; height: 290px; }
  .page--equipment { left: 404px; top: 0; width: 392px; height: 290px; }
  .page--parts { left: 806px; top: 0; width: 394px; height: 290px; }
  .page--planning { left: 0; top: 296px; width: 396px; height: 287px; }
  .page--contact { left: 404px; top: 296px; width: 392px; height: 287px; }

  .topbar { height: 24px; display: flex; align-items: center; justify-content: space-between; padding: 0 8px; }
  .brand { display: flex; align-items: center; gap: 4px; font-size: 8px; font-weight: 700; color: var(--brand); }
  .brand-mark { width: 10px; height: 10px; background: var(--brand); border-radius: 50%; }
  .social { display: flex; gap: 3px; }
  .social span { width: 9px; height: 9px; background: var(--nav); border-radius: 2px; }

  .nav { position: absolute; top: 24px; left: 120px; right: 0; height: 10px; background: linear-gradient(var(--nav), var(--nav-dark)); display: flex; justify-content: flex-end; gap: 9px; padding-right: 8px; align-items: center; }
  .nav a { color: #fff; font-size: 4.6px; text-decoration: none; }

  .banner { position: absolute; top: 34px; left: 0; right: 0; height: 44px; background: linear-gradient(100deg, var(--banner-a), var(--banner-b)); padding: 8px 10px; }
  .banner h1 { font-size: 15px; font-weight: 600; color: var(--ink); line-height: 1.1; }
  .banner p { font-size: 6px; color: var(--muted); margin-top: 2px; width: 110px; line-height: 1.3; }

  .photo { background: linear-gradient(135deg, var(--photo-a), var(--photo-b)); }
  .photo--soft { background: linear-gradient(135deg, #e3eef6, #b8cfe0); }

  .copy { font-size: 4.4px; line-height: 1.45; color: var(--muted); }
  .copy + .copy { margin-top: 4px; }

  .main { position: absolute; top: 86px; left: 10px; width: 250px; }
  .item { display: flex; gap: 6px; margin-bottom: 10px; }
  .item .photo { width: 52px; height: 36px; flex: none; }

  .sidebar { position: absolute; top: 36px; right: 8px; width: 100px; }
  .why { background: #fff; border: 1px solid var(--rule); }
  .why h2 { font-size: 5.6px; font-weight: 700; color: var(--brand-dark); background: var(--side-head); padding: 3px 4px; }
  .why ul { list-style: none; padding: 3px 4px; }
  .why li { font-size: 4.4px; color: var(--ink); padding: 1.3px 0; display: flex; align-items: center; gap: 3px; border-bottom: 1px dotted var(--rule); }
  .why li::before { content: ""; width: 3px; height: 3px; background: var(--nav); border-radius: 50%; }
  .side-photo { height: 34px; margin-top: 6px; }
  .side-note { margin-top: 4px; }
  .badge { margin-top: 6px; width: 46px; height: 16px; background: #fff; border: 1px solid var(--rule); display: flex; align-items: center; padding-left: 3px; }
  .badge span { width: 10px; height: 10px; background: var(--accent); }

  .footer { position: absolute; left: 0; right: 0; bottom: 0; height: 10px; background: var(--footer); border-top: 1px solid var(--rule); font-size: 4.2px; color: var(--muted); padding: 2px 10px; }

  /* home */
  .hero { position: absolute; top: 34px; left: 0; right: 0; height: 66px; }
  .hero-title { position: absolute; top: 44px; left: 170px; }
  .hero-title h1 { font-size: 14px; font-weight: 600; color: var(--ink); }
  .hero-title p { font-size: 6px; color: var(--muted); width: 130px; margin-top: 2px; }
  .home-copy { position: absolute; top: 108px; left: 90px; width: 220px; }
  .tiles { position: absolute; top: 206px; left: 10px; right: 10px; display: flex; gap: 4px; }
  .tile { flex: 1; height: 30px; position: relative; }
  .tile b { position: absolute; left: 0; right: 0; bottom: 0; height: 7px; background: rgba(27,79,134,.85); color: #fff; font-size: 4.2px; font-weight: 600; padding: 1px 3px; }
  .home-links { position: absolute; top: 242px; left: 10px; right: 10px; font-size: 4.2px; color: var(--muted); border-top: 1px solid var(--rule); padding-top: 3px; }

  /* contact */
  .contact-photo { position: absolute; top: 78px; left: 0; width: 150px; height: 150px; background: linear-gradient(90deg, #dce8f1, #ffffff); }
  .address { position: absolute; top: 98px; left: 196px; font-size: 4.8px; line-height: 1.5; color: var(--ink); }
  .address p + p { margin-top: 6px; }
</style>
</head>
<body>

<!-- Home -->
<section class="page page--home">
  <header class="topbar">
    <div class="brand"><span class="brand-mark"></span>ROV Medisource</div>
    <div class="social"><span></span><span></span></div>
  </header>
  <div class="hero photo photo--soft" role="img" aria-label="Hand touching a glowing medical display"></div>
  <nav class="nav"><a>Home</a><a>Equipments</a><a>Accessories &amp; Parts</a><a>Planning &amp; Consulting</a><a>Contact us</a></nav>
  <div class="hero-title">
    <h1>ROV Medisource Inc</h1>
    <p>Magna voluptate excepteur, id ex qui dolor, dolore</p>
  </div>
  <div class="home-copy">
    <p class="copy">ROV Medisource is a leading exporter of used medical equipment worldwide. We source, inspect and ship reliable systems to clinics, hospitals and laboratories, offering fair prices and careful handling for every order.</p>
    <p class="copy">Our team works closely with buyers to match the right equipment to each need, from imaging and monitoring units to surgical tools, parts and accessories for daily care.</p>
    <p class="copy">Every item is checked before export, and we support you with planning, consulting and logistics so your new equipment arrives safely and ready for use.</p>
  </div>
  <div class="tiles">
    <div class="tile photo" role="img" aria-label="Medical equipment"><b>Equipments</b></div>
    <div class="tile photo" role="img" aria-label="Accessories and parts"><b>Accessories &amp; Parts</b></div>
    <div class="tile photo" role="img" aria-label="Planning meeting"><b>Planning &amp; Consulting</b></div>
  </div>
  <div class="home-links">Home · Equipments · Accessories &amp; Parts · Planning &amp; Consulting · Contact us</div>
</section>

<!-- Equipments -->
<section class="page page--equipment">
  <header class="topbar">
    <div class="brand"><span class="brand-mark"></span>ROV Medisource</div>
    <div class="social"><span></span><span></span></div>
  </header>
  <div class="banner"><h1>Equipments</h1><p>Magna voluptate excepteur, id ex qui dolor, dolore</p></div>
  <nav class="nav"><a>Home</a><a>Equipments</a><a>Accessories &amp; Parts</a><a>Planning &amp; Consulting</a><a>Contact us</a></nav>
  <div class="main" style="width:260px">
    <p class="copy">Browse our range of quality used medical equipment, inspected and prepared for export. We offer imaging, monitoring and laboratory systems at fair prices.</p>
    <p class="copy" style="margin-bottom:8px">Each unit is tested by our technicians and shipped with care to buyers around the world.</p>
    <div class="item"><div class="photo" role="img" aria-label="Laboratory machine"></div><p class="copy">Reliable lab analysers and diagnostic units, checked and serviced before delivery. Contact us for current stock, pricing and shipping options to your region.</p></div>
    <div class="item"><div class="photo" role="img" aria-label="Patient monitor"></div><p class="copy">Patient monitors, infusion pumps and surgical devices from trusted makers, ready to support daily care in clinics and hospitals of every size.</p></div>
  </div>
  <aside class="sidebar">
    <div class="why"><h2>Why ROV Medisource?</h2><ul><li>Used Equipment</li><li>Competitive Prices</li><li>Certified Quality</li><li>Worldwide Export</li><li>Trusted Partners</li><li>Fast Delivery</li></ul></div>
    <div class="side-photo photo" role="img" aria-label="Hospital equipment"></div>
    <p class="copy side-note">Ask our team about new arrivals and special offers.</p>
    <div class="badge"><span></span></div>
  </aside>
  <div class="footer">Home · Equipments · Accessories &amp; Parts · Planning &amp; Consulting · Contact us</div>
</section>

<!-- Accessories & Parts -->
<section class="page page--parts">
  <header class="topbar">
    <div class="brand"><span class="brand-mark"></span>ROV Medisource</div>
    <div class="social"><span></span><span></span></div>
  </header>
  <div class="banner"><h1>Accesories &amp; Parts</h1><p>Magna voluptate excepteur, id ex qui dolor, dolore</p></div>
  <nav class="nav"><a>Home</a><a>Equipments</a><a>Accessories &amp; Parts</a><a>Planning &amp; Consulting</a><a>Contact us</a></nav>
  <div class="main" style="width:260px">
    <p class="copy">We supply accessories and spare parts for a wide range of medical systems, helping you extend the life of the equipment you already own.</p>
    <p class="copy" style="margin-bottom:8px">Parts are sourced carefully and checked before shipping.</p>
    <div class="item"><div class="photo" role="img" aria-label="Equipment parts"></div><p class="copy">Probes, cables, batteries and modules for monitors and imaging units. Send us your model details and we will find the right match quickly.</p></div>
    <div class="item"><div class="photo" role="img" aria-label="Medical accessories"></div><p class="copy">Accessories for surgical, lab and patient care devices, packed securely and delivered worldwide with tracking and support from our team.</p></div>
  </div>
  <aside class="sidebar">
    <div class="why"><h2>Why ROV Medisource?</h2><ul><li>Used Equipment</li><li>Competitive Prices</li><li>Certified Quality</li><li>Worldwide Export</li><li>Trusted Partners</li><li>Fast Delivery</li></ul></div>
    <div class="side-photo photo" role="img" aria-label="Hospital equipment"></div>
    <p class="copy side-note">Ask our team about new arrivals and special offers.</p>
    <div class="badge"><span></span></div>
  </aside>
  <div class="footer">Home · Equipments · Accessories &amp; Parts · Planning &amp; Consulting · Contact us</div>
</section>

<!-- Planning & Consulting -->
<section class="page page--planning">
  <header class="topbar">
    <div class="brand"><span class="brand-mark"></span>ROV Medisource</div>
    <div class="social"><span></span><span></span></div>
  </header>
  <div class="banner"><h1>Planning &amp; Consulting</h1><p>Magna voluptate excepteur, id ex qui dolor, dolore</p></div>
  <nav class="nav"><a>Home</a><a>Equipments</a><a>Accessories &amp; Parts</a><a>Planning &amp; Consulting</a><a>Contact us</a></nav>
  <div class="main" style="width:240px">
    <p class="copy">Our consultants help you plan new rooms, wards and labs, choosing equipment that fits your space, budget and care goals.</p>
    <p class="copy">We guide you from first idea to installation, working with your staff to set clear steps, timelines and costs for every project.</p>
    <p class="copy">With years of export experience, we also advise on shipping, customs and local rules so your equipment arrives on time and is ready to use from day one.</p>
  </div>
  <aside class="sidebar">
    <div class="why"><h2>Why ROV Medisource?</h2><ul><li>Used Equipment</li><li>Competitive Prices</li><li>Certified Quality</li><li>Worldwide Export</li><li>Trusted Partners</li><li>Fast Delivery</li></ul></div>
    <div class="side-photo photo" role="img" aria-label="Hospital equipment"></div>
    <p class="copy side-note">Ask our team about new arrivals and special offers.</p>
    <div class="badge"><span></span></div>
  </aside>
  <div class="footer">Home · Equipments · Accessories &amp; Parts · Planning &amp; Consulting · Contact us</div>
</section>

<!-- Contact -->
<section class="page page--contact">
  <header class="topbar">
    <div class="brand"><span class="brand-mark"></span>ROV Medisource</div>
    <div class="social"><span></span><span></span></div>
  </header>
  <div class="banner"><h1>Contact us</h1><p>Magna voluptate excepteur, id ex qui dolor, dolore</p></div>
  <nav class="nav"><a>Home</a><a>Equipments</a><a>Accessories &amp; Parts</a><a>Planning &amp; Consulting</a><a>Contact us</a></nav>
  <div class="contact-photo" role="img" aria-label="Customer service representative"></div>
  <div class="address">
    <p>ROV Medisource Inc<br>Harbor Ave 12<br>Suite 400<br>Northfield<br>Westbury Lane<br>Country</p>
    <p>T: 000 000 0000<br>F: 000 000 0001<br>M: 000 000 0002<br>info@rovmedisource.example</p>
  </div>
  <div class="footer">Home · Equipments · Accessories &amp; Parts · Planning &amp; Consulting · Contact us</div>
</section>

</body>
</html>
```